Request for Business Card Design

Hi. My name is Marlena, I am looking for a new business card design for my company, Quillbrook Sensing Systems, LLC. I really like the design you did for Tavel Harvest and was hoping you could do something similar using our full logo and our mark. I am also open to any raised texture design using our mark. I have attached our full logo, which would need to be somewhere on the card, as well as the mark in both outline and full form, as well as our brand colors / guide. The card does not have to be white, as long as our logo and mark appear. I actually like darker colored business cards more, but am open to all options. If you are interested in working with me, please let me know. We would also take the business card design into letterhead design if you can do that.

```html
<!DOCTYPE html>
<html lang="en">
<head>
<meta charset="utf-8">
<title>Quillbrook Sensing Systems — Business Card</title>
<link rel="stylesheet" href="https://fonts.googleapis.com/css2?family=Source+Sans+3:wght@400;600;700&display=swap">
<style>
  :root {
    --bg: #e6e8ea;
    --card: #ffffff;
    --blue: #1e9bd0;
    --ink: #141414;
    --sky-light: #eef3f7;
    --sky-mid: #c9d7e3;
    --sky-deep: #aebfcf;
    --rule: #9aa6b0;
  }
  * { margin: 0; padding: 0; box-sizing: border-box; }
  html, body { width: 1200px; height: 1157px; overflow: hidden; }
  body {
    background: var(--bg);
    font-family: "Source Sans 3", "Helvetica Neue", Arial, sans-serif;
    color: var(--ink);
    position: relative;
  }
  .card {
    position: absolute;
    width: 720px;
    height: 420px;
    background: var(--card);
    overflow: hidden;
    box-shadow: 0 6px 22px rgba(0,0,0,.12);
  }
  .card--front { left: 110px; top: 80px; }
  .card--back { left: 370px; top: 650px; }

  .sky {
    position: absolute;
    left: 0; right: 0; bottom: 0;
    background: linear-gradient(180deg, rgba(255,255,255,0) 0%, var(--sky-light) 25%, var(--sky-mid) 70%, var(--sky-deep) 100%);
  }
  .card--front .sky { top: 120px; }
  .card--back .sky { top: 150px; opacity: .85; }

  .brand {
    position: absolute;
    display: flex;
    align-items: center;
    gap: 14px;
  }
  .brand__dot {
    width: 46px; height: 46px;
    border-radius: 50%;
    background: var(--blue);
    flex: none;
  }
  .brand__name {
    font-weight: 700;
    text-transform: uppercase;
    color: var(--ink);
    letter-spacing: .02em;
    line-height: 1;
  }
  .card--front .brand { left: 110px; top: 170px; }
  .card--front .brand__name { font-size: 36px; }
  .card--back .brand { left: 250px; top: 58px; }
  .card--back .brand__dot { width: 38px; height: 38px; }
  .card--back .brand__name { font-size: 26px; }

  .band-name {
    position: absolute;
    left: 0; top: 150px;
    width: 640px; height: 58px;
    background: var(--blue);
    border-radius: 0 29px 29px 0;
  }
  .band-title {
    position: absolute;
    left: 0; top: 208px;
    width: 600px; height: 46px;
    background: var(--ink);
    border-radius: 0 0 40px 0;
  }
  .band-badge {
    position: absolute;
    left: 80px; top: 150px;
    width: 104px; height: 104px;
    border-radius: 50%;
    background: var(--card);
    border: 6px solid var(--blue);
  }
  .person__name {
    position: absolute;
    left: 215px; top: 156px;
    font-size: 36px;
    font-weight: 700;
    color: #fff;
    line-height: 1.2;
  }
  .person__role {
    position: absolute;
    left: 215px; top: 215px;
    font-size: 24px;
    color: #fff;
    line-height: 1.3;
  }
  .social {
    position: absolute;
    left: 520px; top: 219px;
    display: flex; gap: 10px;
  }
  .social__dot {
    width: 24px; height: 24px;
    border-radius: 50%;
    background: #fff;
  }

  .contact {
    position: absolute;
    left: 60px; top: 290px;
    list-style: none;
    font-size: 19px;
    line-height: 1.2;
  }
  .contact li { display: flex; align-items: center; gap: 10px; margin-bottom: 12px; }
  .contact svg { width: 18px; height: 18px; flex: none; }
  .divider {
    position: absolute;
    left: 420px; top: 270px;
    width: 1px; height: 110px;
    background: var(--rule);
  }
  .address {
    position: absolute;
    left: 445px; top: 286px;
    display: flex; gap: 8px;
    font-size: 19px;
    line-height: 1.25;
    font-style: normal;
  }
  .address svg { width: 16px; height: 20px; flex: none; margin-top: 2px; }
</style>
</head>
<body>

<section class="card card--front" aria-label="Card front">
  <div class="sky" role="img" aria-label="Soft blue sky with clouds"></div>
  <div class="brand">
    <span class="brand__dot"></span>
    <span class="brand__name">Quillbrook Sensing Systems</span>
  </div>
</section>

<section class="card card--back" aria-label="Card back">
  <div class="sky" role="img" aria-label="Soft blue sky with clouds"></div>
  <div class="brand">
    <span class="brand__dot"></span>
    <span class="brand__name">Quillbrook Sensing Systems</span>
  </div>

  <div class="band-name"></div>
  <div class="band-title"></div>
  <div class="band-badge"></div>
  <h1 class="person__name">Marlena</h1>
  <p class="person__role">Managing Director</p>
  <div class="social"><span class="social__dot"></span><span class="social__dot"></span></div>

  <ul class="contact">
    <li>
      <svg viewBox="0 0 18 18"><rect x="5" y="1" width="8" height="16" rx="1.5" fill="none" stroke="#1e9bd0" stroke-width="1.8"/><line x1="8" y1="14" x2="10" y2="14" stroke="#1e9bd0" stroke-width="1.6"/></svg>
      +001 555 210 4837
    </li>
    <li>
      <svg viewBox="0 0 18 18"><rect x="2" y="7" width="14" height="9" rx="1.5" fill="#1e9bd0"/><rect x="5" y="2" width="6" height="6" fill="#1e9bd0"/></svg>
      +001 555 210 9062
    </li>
    <li>
      <svg viewBox="0 0 18 18"><circle cx="9" cy="9" r="7.5" fill="none" stroke="#1e9bd0" stroke-width="1.6"/><ellipse cx="9" cy="9" rx="3.2" ry="7.5" fill="none" stroke="#1e9bd0" stroke-width="1.4"/><line x1="1.5" y1="9" x2="16.5" y2="9" stroke="#1e9bd0" stroke-width="1.4"/></svg>
      www.quillbrooksensing.com
    </li>
  </ul>

  <div class="divider"></div>
  <address class="address">
    <svg viewBox="0 0 16 20"><path d="M8 1a6 6 0 0 0-6 6c0 4.5 6 12 6 12s6-7.5 6-12a6 6 0 0 0-6-6z" fill="#1e9bd0"/><circle cx="8" cy="7" r="2.2" fill="#fff"/></svg>
    <span>1180 Harlow Ridge<br>Road • Fenwick, CO<br>80999</span>
  </address>
</section>

</body>
</html>
```